Sundial Bail Bonds Signboard Ad

I need a signboard ad that will be posted at a jail. We are a bail bond company and we bail people out of jail. The inmate/customer will call our company when they see our signboard ad posted inside a jail. The goal of the signboard ad is to get the attention of a person in custody and to stand out from the competition. The signboard ad is about 5x7. Open to any colors that will make it stand out. The content of the signboard ad must have "Sundial Bail Bonds" and our company phone number: (555) 318-2746. We want to emphasize we can get them out of jail quick and fast, was thinking maybe a catch phrase of "Sundial outta Jail" or "Sundial to Freedom". We don't have a logo. I will upload an attachment to show what the competition looks like. As you will see in the upload, my ad will go along with my competition. Also, I'm open to any creative ideas that will make my signboard ad stand out. Thank You.

Target Market(s)

People in jail.

Requirements
Must have
• Sundial Bail Bonds

(555) 318-2746
Nice to have
• I'm open to catch phrases that will get attention, for example "Sundial outta Jail" or "Sundial to Freedom". I do not have a company logo, if you can create a company logo, would be nice, was thinking an image of a rocket blasting off, The name of company is Sundial Bail Bonds.

```html
<!DOCTYPE html>
<html lang="en">
<head>
<meta charset="utf-8">
<title>Sundial Bail Bonds Signboard</title>
<link rel="stylesheet" href="https://fonts.googleapis.com/css2?family=Anton&family=Montserrat:wght@500;700&display=swap">
<style>
  :root {
    --page-bg: #dedede;
    --sign-black: #000000;
    --sign-white: #ffffff;
    --headline-yellow: #ffed2b;
    --band-yellow: #ffff00;
    --ink: #000000;
  }
  * { margin: 0; padding: 0; box-sizing: border-box; }
  html, body {
    width: 1200px;
    height: 1200px;
    overflow: hidden;
    background: var(--page-bg);
  }
  .signboard {
    position: absolute;
    left: 138px;
    top: 270px;
    width: 924px;
    height: 660px;
    background: var(--sign-black);
    overflow: hidden;
  }
  .brand {
    position: absolute;
    top: 80px;
    left: 0;
    width: 100%;
    display: flex;
    justify-content: center;
    align-items: center;
    gap: 14px;
    white-space: nowrap;
  }
  .brand-mark {
    width: 46px;
    height: 46px;
    border-radius: 50%;
    background: var(--sign-white);
  }
  .brand-name {
    font-family: "Montserrat", sans-serif;
    font-weight: 500;
    font-size: 32px;
    line-height: 1;
    color: var(--sign-white);
    letter-spacing: 1px;
  }
  .headline {
    position: absolute;
    top: 188px;
    left: 0;
    width: 100%;
    text-align: center;
    font-family: "Anton", sans-serif;
    font-weight: 400;
    font-size: 170px;
    line-height: 1;
    color: var(--sign-white);
    letter-spacing: 6px;
    white-space: nowrap;
  }
  .tagline {
    position: absolute;
    top: 356px;
    left: 0;
    width: 100%;
    text-align: center;
    font-family: "Montserrat", sans-serif;
    font-weight: 700;
    font-size: 106px;
    line-height: 1.1;
    color: var(--headline-yellow);
    letter-spacing: 6px;
    white-space: nowrap;
  }
  .phone-band {
    position: absolute;
    top: 486px;
    left: 138px;
    right: 0;
    height: 126px;
    background: var(--band-yellow);
  }
  .phone-badge {
    position: absolute;
    left: 43px;
    top: 481px;
    width: 136px;
    height: 136px;
    border-radius: 50%;
    background: var(--sign-white);
    display: flex;
    align-items: center;
    justify-content: center;
  }
  .phone-badge svg { width: 66px; height: 66px; }
  .phone-number {
    position: absolute;
    top: 500px;
    left: 188px;
    right: 30px;
    text-align: center;
    font-family: "Anton", sans-serif;
    font-size: 98px;
    line-height: 1;
    color: var(--ink);
    letter-spacing: 4px;
    white-space: nowrap;
  }
</style>
</head>
<body>
  <main class="signboard">
    <div class="brand">
      <span class="brand-mark"></span>
      <span class="brand-name">SUNDIAL BAIL BONDS</span>
    </div>
    <h1 class="headline">SUNDIAL</h1>
    <p class="tagline">to Freedom</p>
    <div class="phone-band"></div>
    <div class="phone-badge">
      <svg viewBox="0 0 64 64" aria-hidden="true">
        <path d="M14 8c3-2 6-1 7 2l5 10c1 2 0 4-2 5l-4 3c3 7 8 12 15 15l3-4c1-2 3-3 5-2l10 5c3 1 4 4 2 7l-3 4c-3 3-7 4-11 2C27 50 14 37 9 23c-2-4-1-8 2-11z" fill="#000"/>
        <path d="M38 10a18 18 0 0 1 16 16" fill="none" stroke="#000" stroke-width="4" stroke-linecap="round"/>
        <path d="M37 18a10 10 0 0 1 9 9" fill="none" stroke="#000" stroke-width="4" stroke-linecap="round"/>
      </svg>
    </div>
    <p class="phone-number">(555) 318-2746</p>
  </main>
</body>
</html>
```